Redesign website for small print company

Vindaborgprent is a small printing company in Iceland mainly servicing Students, schools, etc. We are also doing all kind of other jobs, like business cards, book printing, brochure printing etc. We are also selling books online.
Our website is: www.vindaborgprent.is
What we are looking for is:
- Web Design (Uncoded - PSD layout only)
- Mobile friendly design, using our current color scheme: Red, green, yellow and light gray.
- Clean simple design
- Simple, light and easy to use.
- More menu Items/drop down
Industry/Entity Type
Digital Printing
Number of Pages Required
5+ page
Requirements
Must have
- Easy navigation
- Designed for mobile
- Current color scheme (see logo)
Nice to have
- Icon based products

```html
<!DOCTYPE html>
<html lang="en">
<head>
<meta charset="utf-8">
<title>Vindaborgprent – Printing Services</title>
<link href="https://fonts.googleapis.com/css2?family=Montserrat:wght@400;600;700;800&family=Open+Sans:wght@400;600;700&display=swap" rel="stylesheet">
<style>
:root{
  --red:#e8392f;
  --green:#0f6b3a;
  --yellow:#f7c614;
  --orange:#f59b1c;
  --dark:#151515;
  --light:#f1f1f1;
  --grey:#6d6d6d;
  --white:#fff;
}
*{margin:0;padding:0;box-sizing:border-box}
html,body{width:1200px;height:4523px;overflow:hidden}
body{font-family:"Open Sans",Arial,sans-serif;color:#333;background:var(--white);position:relative}
h1,h2,h3,h4,.nav a,.btn{font-family:"Montserrat",Arial,sans-serif}
section,header,footer{position:absolute;left:0;width:1200px;overflow:hidden}
.btn{display:inline-flex;align-items:center;gap:8px;border-radius:22px;font-size:11px;font-weight:700;text-transform:uppercase;padding:0 22px;height:32px;color:var(--white)}
.btn svg{width:14px;height:10px}
.btn-yellow{background:var(--yellow);color:var(--dark)}
.btn-green{background:var(--green)}
.btn-red{background:var(--red)}
.btn-black{background:var(--dark)}
.sec-title{text-align:center;font-size:30px;font-weight:800;text-transform:uppercase;letter-spacing:.5px}
.sec-title .hl{color:var(--red)}

/* header */
.topbar{top:0;height:27px;background:var(--green);color:var(--white);font-size:11px}
.topbar .info{position:absolute;left:380px;top:6px;display:flex;gap:26px}
.topbar .info span{display:flex;align-items:center;gap:6px}
.topbar .lang{margin-left:8px}
.nav-bar{top:27px;height:58px;background:var(--white);box-shadow:0 2px 6px rgba(0,0,0,.08);z-index:2;overflow:visible}
.brand{position:absolute;left:14px;top:-24px;width:84px;height:104px;background:var(--white);border:3px solid var(--green);display:flex;flex-direction:column;align-items:center;justify-content:center;gap:6px;z-index:3}
.brand .mark{width:34px;height:34px;background:var(--red)}
.brand .name{font-family:"Montserrat",sans-serif;font-weight:700;font-size:8.5px;color:var(--green)}
.nav{position:absolute;left:340px;top:0;height:58px;display:flex;align-items:center}
.nav a{font-size:11px;font-weight:600;text-transform:uppercase;color:#333;text-decoration:none;padding:0 19px;height:58px;display:flex;align-items:center;border-right:1px solid #eee}
.nav a.active{color:var(--red)}
.cart{position:absolute;left:930px;top:16px;display:flex;align-items:center;gap:8px}
.cart .ico{width:18px;height:18px}
.cart .pill{background:var(--red);color:#fff;font-size:9px;font-weight:700;border-radius:10px;padding:5px 12px;font-family:"Montserrat",sans-serif}

/* hero */
.hero{top:85px;height:533px}
.hero .photo{position:absolute;inset:0;background:linear-gradient(160deg,#d9dde2 0%,#a7b3be 40%,#7e8c99 70%,#c3c9cf 100%)}
.hero .shade{position:absolute;inset:0;background:rgba(0,0,0,.18)}
.hero .copy{position:absolute;left:0;width:100%;top:205px;text-align:center;color:#fff}
.hero h2{font-size:24px;font-weight:700;letter-spacing:1px}
.hero h1{font-size:38px;font-weight:700;letter-spacing:1px;margin-top:4px}
.hero h1 .p{color:var(--yellow)}
.hero .btn{margin-top:18px}
.hero .arrow{position:absolute;top:250px;width:20px;height:34px}

/* welcome */
.welcome{top:618px;height:422px;background:var(--white)}
.welcome .pic{position:absolute;left:211px;top:52px;width:318px;height:310px;border:5px solid var(--red);background:linear-gradient(135deg,#8aa0b2,#cfd7de 55%,#5d7388)}
.welcome .txt{position:absolute;left:552px;top:52px;width:430px}
.welcome h3{font-size:18px;font-weight:700;color:var(--red)}
.welcome h2{font-size:21px;font-weight:800;color:var(--green);margin-top:4px}
.welcome .lead{font-size:11.5px;font-weight:700;color:#333;line-height:17px;margin-top:16px}
.welcome p{font-size:11px;line-height:17px;color:var(--grey);margin-top:8px}
.welcome .btn{margin-top:22px}

/* services */
.services{top:1040px;height:407px;background:var(--light)}
.services .band{position:absolute;left:0;top:0;width:100%;height:302px;background:linear-gradient(180deg,#111 0%,#2a2a2a 100%)}
.services .sec-title{position:absolute;top:50px;width:100%;color:#fff}
.svc{position:absolute;top:120px;width:170px;height:167px;background:var(--red)}
.svc .top{position:absolute;left:0;top:0;width:100%;height:62px;background:var(--yellow)}
.svc .tile{position:absolute;left:50px;top:48px;width:70px;height:70px;background:#fff;border-radius:8px;display:flex;align-items:center;justify-content:center;box-shadow:0 2px 6px rgba(0,0,0,.15)}
.svc .tile svg{width:34px;height:34px}
.svc-label{position:absolute;top:350px;width:220px;text-align:center;font-size:13px;font-weight:600;text-transform:uppercase;color:#222;font-family:"Montserrat",sans-serif}

/* products */
.products{top:1447px;height:543px;background:var(--light)}
.products .sec-title{position:absolute;top:28px;width:100%}
.card{position:absolute;top:94px;width:236px;height:359px;background:#fff;box-shadow:0 2px 8px rgba(0,0,0,.08);text-align:center}
.card .img{height:193px}
.card .badge{position:absolute;left:96px;top:172px;width:44px;height:44px;border-radius:50%;background:var(--yellow);display:flex;align-items:center;justify-content:center}
.card .badge i{width:22px;height:22px;border-radius:50%;background:var(--red);display:block}
.card h4{font-size:13px;font-weight:700;margin-top:40px;text-transform:uppercase}
.card p{font-size:10px;line-height:14px;color:var(--grey);padding:6px 30px 0}
.card .btn{position:absolute;left:54px;bottom:0;height:26px;border-radius:0;width:128px;justify-content:center;font-size:10px}
.products .all{position:absolute;left:537px;top:483px;height:28px}

/* audience */
.audience{top:1990px;height:341px;background:#fff}
.audience .sec-title{position:absolute;top:75px;width:100%;color:#222}
.aud{position:absolute;top:150px;width:200px;text-align:center}
.aud .circle{width:94px;height:94px;border-radius:50%;margin:0 auto;display:flex;align-items:center;justify-content:center;border:6px solid #fff;box-shadow:0 0 0 2px #ddd}
.aud .circle svg{width:40px;height:40px}
.aud h4{font-size:13px;font-weight:700;margin-top:28px;text-transform:uppercase}

/* books */
.books{top:2331px;height:337px;background:var(--red)}
.books .yel{position:absolute;left:0;top:0;width:100%;height:100%}
.books .cover{position:absolute;left:235px;top:50px;width:180px;height:250px;background:linear-gradient(160deg,#f7f3ea,#e8e2d6);box-shadow:4px 6px 14px rgba(0,0,0,.3)}
.books .cover .art{position:absolute;left:25px;top:60px;width:130px;height:150px;background:radial-gradient(circle at 50% 55%,#3b6d5a,#c0474a 45%,#f4efe4 75%)}
.books .txt{position:absolute;left:491px;top:80px;width:440px;color:#fff}
.books h2{font-size:25px;font-weight:700;text-transform:uppercase}
.books p{font-size:11px;line-height:17px;margin-top:14px;opacity:.95}
.books .price{font-size:13px;font-weight:700;margin-top:12px;font-family:"Montserrat",sans-serif}
.books .btn{margin-top:18px}

/* printlife */
.printlife{top:2668px;height:498px;background:#fff}
.printlife .sec-title{position:absolute;top:125px;width:100%;color:#222;font-size:27px}
.printlife .frame{position:absolute;left:471px;top:178px;width:262px;height:262px;border:2px solid #222;background:var(--yellow);display:flex;flex-direction:column;align-items:center;justify-content:center;gap:14px;overflow:visible}
.printlife .frame .sq{width:60px;height:60px;background:var(--red)}
.printlife .frame .nm{font-family:"Montserrat",sans-serif;font-weight:700;font-size:20px;color:var(--green)}
.printlife .frame .btn{position:absolute;bottom:-16px;left:56px}
.feat{position:absolute;width:220px;display:flex;flex-direction:column;gap:10px}
.feat .ic{width:44px;height:44px;border-radius:50%;display:flex;align-items:center;justify-content:center}
.feat .ic svg{width:22px;height:22px}
.feat h4{font-size:14px;font-weight:700;line-height:18px}
.feat.left{left:272px;align-items:flex-start}
.feat.right{left:708px;align-items:flex-end;text-align:right}
.feat::after{content:"";position:absolute;top:22px;height:1px;width:110px;border-top:1px dashed #999}
.feat.left::after{left:56px}
.feat.right::after{right:56px}

/* testimonials */
.testi{top:3166px;height:346px;background:var(--green)}
.testi .sec-title{position:absolute;top:75px;width:100%;color:#fff;font-size:27px}
.testi .sec-title .p{color:var(--yellow)}
.quote{position:absolute;top:152px;width:365px;height:108px;background:#fff;padding:18px 20px;overflow:visible}
.quote p{font-size:10.5px;line-height:16px;color:#444;width:255px}
.quote .qm{position:absolute;right:22px;top:18px;font-family:Georgia,serif;font-size:70px;line-height:60px;color:#d8d8d8}
.quote .who{position:absolute;left:20px;top:124px;display:flex;align-items:center;gap:8px;color:#fff;font-size:11px;font-weight:700}
.quote .stars{color:var(--yellow);letter-spacing:1px;font-size:10px}
.quote .ava{position:absolute;width:62px;height:62px;border-radius:50%;background:#c9cfd4;border:4px solid #fff;top:86px}
.testi .arrow{position:absolute;top:230px;width:14px;height:22px}

/* steps */
.steps{top:3512px;height:543px;background:#fff}
.steps .sec-title{position:absolute;top:62px;width:100%;color:#222;font-size:27px}
.step{position:absolute;width:160px;text-align:center}
.step .c{width:96px;height:96px;border-radius:50%;margin:0 auto;display:flex;align-items:center;justify-content:center}
.step .c svg{width:40px;height:40px}
.step .n{font-family:"Montserrat",sans-serif;font-size:13px;font-weight:700;color:var(--red)}
.step h4{font-size:13px;font-weight:700;line-height:17px;color:#222}

/* cta */
.cta{top:4055px;height:166px;background:var(--yellow);text-align:center}
.cta h3{font-size:13px;font-weight:600;color:#fff;margin-top:40px;letter-spacing:1px}
.cta h2{font-size:26px;font-weight:800;color:#fff;margin-top:4px}
.cta .btn{margin-top:12px;height:28px}

/* footer */
.footer{top:4221px;height:271px;background:linear-gradient(180deg,#1b1b1b,#101010)}
.fcol{position:absolute;top:54px;color:#ccc}
.fcol h4{font-size:13px;font-weight:700;color:#fff;margin-bottom:16px;text-transform:uppercase}
.fcol li{list-style:none;font-size:10.5px;line-height:22px;display:flex;align-items:center;gap:8px;text-transform:uppercase}
.fcol li::before{content:"›";color:var(--yellow)}
.fcol .row{display:flex;gap:10px;font-size:10.5px;line-height:16px;margin-bottom:14px;align-items:flex-start}
.fcol .row svg{width:14px;height:14px;flex:none}
.map{width:180px;height:120px;background:linear-gradient(135deg,#e9ecee,#d3d8dc)}
.fcol p{font-size:10.5px;line-height:16px;width:200px}
.sub{display:flex;margin-top:14px;width:190px;height:26px;background:#fff}
.sub span{flex:1;font-size:9.5px;color:#888;padding:7px 8px}
.sub i{width:26px;background:var(--red)}
.bottom{top:4492px;height:31px;background:#0a0a0a;color:#999;font-size:9.5px}
.bottom .copy{position:absolute;left:196px;top:9px}
.social{position:absolute;left:895px;top:6px;display:flex;gap:6px}
.social i{width:19px;height:19px;border-radius:50%;background:var(--red);display:block}
</style>
</head>
<body>

<header class="topbar">
  <div class="info">
    <span><svg width="11" height="11" viewBox="0 0 24 24"><path fill="#fff" d="M6.6 10.8a15 15 0 006.6 6.6l2.2-2.2c.3-.3.7-.4 1-.2 1.1.4 2.3.6 3.6.6.6 0 1 .4 1 1V20c0 .6-.4 1-1 1A17 17 0 013 4c0-.6.4-1 1-1h3.5c.6 0 1 .4 1 1 0 1.3.2 2.5.6 3.6.1.3 0 .7-.2 1z"/></svg>555 0142</span>
    <span><svg width="12" height="10" viewBox="0 0 24 18"><path fill="#fff" d="M0 0h24v18H0z"/><path fill="#0f6b3a" d="M0 0l12 9 12-9v3l-12 9L0 3z"/></svg>verk@vindaborgprent.is</span>
    <span><svg width="11" height="11" viewBox="0 0 24 24"><circle cx="12" cy="12" r="10" fill="none" stroke="#fff" stroke-width="2.5"/><path d="M12 6v6l4 3" stroke="#fff" stroke-width="2.5" fill="none"/></svg>Mon – Fri: 9–17</span>
    <span class="lang">ISK ▾</span>
  </div>
</header>

<header class="nav-bar">
  <div class="brand"><span class="mark"></span><span class="name">Vindaborgprent</span></div>
  <nav class="nav">
    <a class="active">Home</a><a>About Us</a><a>Services</a><a>Product</a><a>Job Submit</a><a>Contact Us</a>
  </nav>
  <div class="cart">
    <svg class="ico" viewBox="0 0 24 24"><path d="M2 3h3l3 12h11l2-8H7" fill="none" stroke="#f7c614" stroke-width="2.4"/><circle cx="9" cy="20" r="1.8" fill="#f7c614"/><circle cx="18" cy="20" r="1.8" fill="#f7c614"/></svg>
    <span class="pill">View Cart</span>
  </div>
</header>

<section class="hero">
  <div class="photo" role="img" aria-label="Photo of a gloved hand checking freshly printed sheets on a press"></div>
  <div class="shade"></div>
  <svg class="arrow" style="left:18px" viewBox="0 0 20 34"><path d="M17 2L3 17l14 15" fill="none" stroke="#fff" stroke-width="2"/></svg>
  <svg class="arrow" style="right:18px" viewBox="0 0 20 34"><path d="M3 2l14 15L3 32" fill="none" stroke="#fff" stroke-width="2"/></svg>
  <div class="copy">
    <h2>HIGH QUALITY</h2>
    <h1><span class="p">P</span>RINTING SERVICES</h1>
    <span class="btn btn-yellow">Contact Us <svg viewBox="0 0 14 10"><path d="M0 5h12M8 1l4 4-4 4" fill="none" stroke="#151515" stroke-width="1.6"/></svg></span>
  </div>
</section>

<section class="welcome">
  <div class="pic" role="img" aria-label="Photo of two print workers in hard hats at a control desk"></div>
  <div class="txt">
    <h3>WELCOME TO</h3>
    <h2>VELKOMIN Í VINDABORGPRENT</h2>
    <p class="lead">Vindaborgprent er lítil prentsmiðja sem þjónar nemendum, skólum og fyrirtækjum um allt land með vandaðri og hraðri prentun á góðu verði.</p>
    <p>Við prentum ritgerðir, nafnspjöld, bækur og bæklinga og bjóðum einnig upp á hönnun, innbindingu og sendingu heim. Markmið okkar er einföld þjónusta, stuttur afgreiðslutími og falleg útkoma í hvert sinn sem þú pantar hjá okkur.</p>
    <span class="btn btn-green">Read More <svg viewBox="0 0 14 10"><path d="M0 5h12M8 1l4 4-4 4" fill="none" stroke="#fff" stroke-width="1.6"/></svg></span>
  </div>
</section>

<section class="services">
  <div class="band" role="img" aria-label="Dark photo of a printing press"></div>
  <h2 class="sec-title">Our Services</h2>
  <div class="svc" style="left:265px"><div class="top"></div><div class="tile"><svg viewBox="0 0 24 24"><rect x="3" y="6" width="18" height="12" rx="1" fill="#0f6b3a"/><rect x="6" y="9" width="5" height="5" fill="#fff"/><path d="M13 10h6M13 13h5" stroke="#fff" stroke-width="1.4"/></svg></div></div>
  <div class="svc" style="left:513px"><div class="top"></div><div class="tile"><svg viewBox="0 0 24 24"><rect x="6" y="3" width="12" height="18" fill="#0f6b3a"/><path d="M9 8h6M9 11h6M9 14h4" stroke="#fff" stroke-width="1.4"/></svg></div></div>
  <div class="svc" style="left:763px"><div class="top"></div><div class="tile"><svg viewBox="0 0 24 24"><path d="M4 5l6 2v13l-6-2zM10 7l5-2v13l-5 2zM15 5l5 2v13l-5-2z" fill="#0f6b3a"/></svg></div></div>
  <div class="svc-label" style="left:240px">Business Cards</div>
  <div class="svc-label" style="left:488px">Book Printing</div>
  <div class="svc-label" style="left:738px">Brochure Printing</div>
</section>

<section class="products">
  <h2 class="sec-title"><span class="hl">Our</span> Products</h2>
  <div class="card" style="left:211px">
    <div class="img" role="img" aria-label="Photo of bound essays and reports" style="background:linear-gradient(135deg,#eef0f2,#c9ced3)"></div>
    <div class="badge"><i></i></div>
    <h4>Essays</h4>
    <p>Clean bound essays and theses printed fast, ready for hand-in the same day.</p>
    <span class="btn btn-black">View More</span>
  </div>
  <div class="card" style="left:482px">
    <div class="img" role="img" aria-label="Photo of stacked black business cards" style="background:linear-gradient(135deg,#555,#1c1c1c 60%,#888)"></div>
    <div class="badge"><i></i></div>
    <h4>Business Cards</h4>
    <p>Sharp business cards on quality stock in any finish, printed in small runs.</p>
    <span class="btn btn-green">View More</span>
  </div>
  <div class="card" style="left:751px">
    <div class="img" role="img" aria-label="Photo of printed leaflets and flyers" style="background:linear-gradient(135deg,#d8e1ea,#7c93ad 60%,#e8c25a)"></div>
    <div class="badge"><i></i></div>
    <h4>Leaflets</h4>
    <p>Colourful leaflets and flyers for events, shops and schools at fair prices.</p>
    <span class="btn btn-black">View More</span>
  </div>
  <span class="btn btn-red all">View All <svg viewBox="0 0 14 10"><path d="M0 5h12M8 1l4 4-4 4" fill="none" stroke="#fff" stroke-width="1.6"/></svg></span>
</section>

<section class="audience">
  <h2 class="sec-title"><span class="hl">Services</span> We Serve</h2>
  <div class="aud" style="left:265px"><div class="circle" style="background:var(--yellow)"><svg viewBox="0 0 24 24"><circle cx="12" cy="8" r="3" fill="#151515"/><circle cx="5.5" cy="10" r="2.3" fill="#151515"/><circle cx="18.5" cy="10" r="2.3" fill="#151515"/><path d="M6 20c0-4 2.7-6 6-6s6 2 6 6zM1 20c0-3 2-4.5 4.5-4.5M23 20c0-3-2-4.5-4.5-4.5" fill="#151515"/></svg></div><h4>Students</h4></div>
  <div class="aud" style="left:506px"><div class="circle" style="background:var(--red)"><svg viewBox="0 0 24 24"><path d="M12 3l9 5H3z" fill="#fff"/><rect x="4" y="9" width="16" height="11" fill="#fff"/><path d="M7 11v7M11 11v7M15 11v7" stroke="#e8392f" stroke-width="1.6"/></svg></div><h4>Schools</h4></div>
  <div class="aud" style="left:747px"><div class="circle" style="background:var(--green)"><svg viewBox="0 0 24 24"><rect x="3" y="8" width="18" height="12" rx="1" fill="#fff"/><path d="M9 8V5h6v3" fill="none" stroke="#fff" stroke-width="2"/><path d="M3 13h18" stroke="#0f6b3a" stroke-width="1.4"/></svg></div><h4>Business</h4></div>
</section>

<section class="books">
  <svg class="yel" viewBox="0 0 1200 337" preserveAspectRatio="none"><polygon points="0,0 380,0 250,337 0,337" fill="#f7c614"/></svg>
  <div class="cover"><div class="art" role="img" aria-label="Book cover with colourful splash artwork"></div></div>
  <div class="txt">
    <h2>Buy Books Online</h2>
    <p>Skoðaðu úrval bóka sem við prentum og gefum út. Pantaðu á netinu og fáðu bókina senda heim að dyrum á örfáum dögum, hvar sem þú ert á landinu.</p>
    <p>Nýjar bækur bætast við reglulega og nemendur fá sérstakan afslátt af völdum titlum út skólaárið.</p>
    <div class="price">4.990 kr</div>
    <span class="btn btn-green">Buy Now <svg viewBox="0 0 14 10"><path d="M0 5h12M8 1l4 4-4 4" fill="none" stroke="#fff" stroke-width="1.6"/></svg></span>
  </div>
</section>

<section class="printlife">
  <h2 class="sec-title"><span class="hl">We Make</span> Your <span class="hl">P</span>rintlife Better</h2>
  <div class="frame">
    <span class="sq"></span>
    <span class="nm">Vindaborgprent</span>
    <span class="btn btn-green">Contact Us Now <svg viewBox="0 0 14 10"><path d="M0 5h12M8 1l4 4-4 4" fill="none" stroke="#fff" stroke-width="1.6"/></svg></span>
  </div>
  <div class="feat left" style="top:208px"><div class="ic" style="background:var(--yellow)"><svg viewBox="0 0 24 24"><rect x="3" y="6" width="18" height="12" rx="1" fill="#151515"/><path d="M3 10h18" stroke="#f7c614" stroke-width="2"/></svg></div><h4>Secured<br>Payment</h4></div>
  <div class="feat left" style="top:365px"><div class="ic" style="background:var(--red)"><svg viewBox="0 0 24 24"><path d="M5 19l2-6 9-9 4 4-9 9z" fill="#fff"/></svg></div><h4>Creating Design<br>Of Your Own</h4></div>
  <div class="feat right" style="top:208px"><div class="ic" style="background:var(--yellow)"><svg viewBox="0 0 24 24"><circle cx="12" cy="12" r="8" fill="none" stroke="#151515" stroke-width="2"/><path d="M4 12h16M12 4c-3 3-3 13 0 16M12 4c3 3 3 13 0 16" fill="none" stroke="#151515" stroke-width="1.4"/></svg></div><h4>Eco Friendly<br>Materials</h4></div>
  <div class="feat right" style="top:365px"><div class="ic" style="background:var(--red)"><svg viewBox="0 0 24 24"><path d="M3 11l9-7 9 7v9h-6v-5h-6v5H3z" fill="#fff"/></svg></div><h4>Home Delivery<br>Options</h4></div>
</section>

<section class="testi">
  <h2 class="sec-title">What <span class="p">P</span>eople Are Saying About Us</h2>
  <svg class="arrow" style="left:190px" viewBox="0 0 14 22"><path d="M12 2L3 11l9 9" fill="none" stroke="#fff" stroke-width="2"/></svg>
  <svg class="arrow" style="left:1000px" viewBox="0 0 14 22"><path d="M2 2l9 9-9 9" fill="none" stroke="#fff" stroke-width="2"/></svg>
  <div class="quote" style="left:226px">
    <p>Fast, friendly service and my thesis looked perfect. I will order all my school printing here from now on, highly recommended.</p>
    <span class="qm">“</span>
    <div class="ava" style="left:150px" role="img" aria-label="Customer portrait"></div>
    <div class="who">Anna Berg <span class="stars">★★★★★</span></div>
  </div>
  <div class="quote" style="left:612px">
    <p>Our business cards arrived quickly and the quality was excellent. Great prices and a team that really cares about detail.</p>
    <span class="qm">“</span>
    <div class="ava" style="left:290px" role="img" aria-label="Customer portrait"></div>
    <div class="who" style="left:130px">Jon Dale <span class="stars">★★★★★</span></div>
  </div>
</section>

<section class="steps">
  <h2 class="sec-title"><span class="hl">How</span> It Work</h2>
  <svg style="position:absolute;left:0;top:0" width="1200" height="543"><path d="M265 227 C330 120 380 110 431 127 S540 260 600 257 S700 120 769 127 S880 220 929 227" fill="none" stroke="#bbb" stroke-width="1.5" stroke-dasharray="5 5"/></svg>
  <div class="step" style="left:185px;top:179px"><div class="c" style="background:var(--red)"><svg viewBox="0 0 24 24"><path d="M6 3h9l4 4v14H6z" fill="#fff"/><path d="M12 10v7M9 13l3-3 3 3" stroke="#e8392f" stroke-width="1.6" fill="none"/></svg></div><div class="n" style="margin-top:10px">1</div><h4>Select or Upload</h4></div>
  <div class="step" style="left:351px;top:100px"><div class="n">2</div><h4 style="margin-bottom:8px">Customize It<br>by Your Choise</h4><div class="c" style="background:var(--yellow)"><svg viewBox="0 0 24 24"><rect x="3" y="4" width="18" height="12" rx="1" fill="#fff"/><path d="M9 20h6M12 16v4" stroke="#fff" stroke-width="2"/></svg></div></div>
  <div class="step" style="left:520px;top:209px"><div class="c" style="background:var(--green)"><svg viewBox="0 0 24 24"><path d="M3 11h4v9H3zM8 20V11l4-7c1.5 0 2 1 2 2l-1 4h6c1 0 2 1 1.7 2l-1.7 7c-.2.7-.8 1-1.5 1z" fill="#fff"/></svg></div><div class="n" style="margin-top:10px">3</div><h4>Finalize</h4></div>
  <div class="step" style="left:689px;top:100px"><h4>Checkout &amp; Add<br>Your Details</h4><div class="n" style="margin-bottom:8px">4</div><div class="c" style="background:var(--dark)"><svg viewBox="0 0 24 24"><rect x="6" y="3" width="12" height="18" fill="#fff"/><path d="M9 8h6M9 11h6M9 14h6" stroke="#151515" stroke-width="1.4"/></svg></div></div>
  <div class="step" style="left:849px;top:179px"><div class="c" style="background:var(--orange)"><svg viewBox="0 0 24 24"><circle cx="12" cy="12" r="9" fill="none" stroke="#fff" stroke-width="2"/><circle cx="9" cy="10" r="1.3" fill="#fff"/><circle cx="15" cy="10" r="1.3" fill="#fff"/><path d="M8 14c2 3 6 3 8 0" stroke="#fff" stroke-width="1.8" fill="none"/></svg></div><div class="n" style="margin-top:10px">5</div><h4>Enjoy Your<br>Product</h4></div>
</section>

<section class="cta">
  <h3>WE ARE READY TO HELP YOU</h3>
  <h2>GET THE BEST SERVICE TODAY!</h2>
  <span class="btn btn-black">Contact Us Today <svg viewBox="0 0 14 10"><path d="M0 5h12M8 1l4 4-4 4" fill="none" stroke="#fff" stroke-width="1.6"/></svg></span>
</section>

<footer class="footer">
  <div class="fcol" style="left:196px"><h4>Quick Links</h4><ul><li>Home</li><li>About Us</li><li>Our Services</li><li>Products</li><li>Job Submit</li><li>Contact Us</li></ul></div>
  <div class="fcol" style="left:347px"><h4>Contact Information</h4>
    <div class="row"><svg viewBox="0 0 24 24"><path d="M12 2a7 7 0 00-7 7c0 5 7 13 7 13s7-8 7-13a7 7 0 00-7-7z" fill="#f7c614"/><circle cx="12" cy="9" r="2.5" fill="#151515"/></svg><span>Lindargata 9<br>Reykjavík Iceland</span></div>
    <div class="row"><svg viewBox="0 0 24 24"><path fill="#f7c614" d="M6.6 10.8a15 15 0 006.6 6.6l2.2-2.2c.3-.3.7-.4 1-.2 1.1.4 2.3.6 3.6.6.6 0 1 .4 1 1V20c0 .6-.4 1-1 1A17 17 0 013 4c0-.6.4-1 1-1h3.5c.6 0 1 .4 1 1 0 1.3.2 2.5.6 3.6.1.3 0 .7-.2 1z"/></svg><span>555 0142</span></div>
    <div class="row"><svg viewBox="0 0 24 18"><path fill="#f7c614" d="M0 0h24v18H0z"/><path fill="#151515" d="M0 0l12 9 12-9v3l-12 9L0 3z"/></svg><span>verk@vindaborgprent.is</span></div>
    <div class="row"><svg viewBox="0 0 24 24"><circle cx="12" cy="12" r="10" fill="none" stroke="#f7c614" stroke-width="2.5"/><path d="M12 6v6l4 3" stroke="#f7c614" stroke-width="2.5" fill="none"/></svg><span>Mon – Fri: 9–17</span></div>
  </div>
  <div class="fcol" style="left:573px"><h4>Find Us On Map</h4><div class="map" role="img" aria-label="Street map showing the shop location"></div></div>
  <div class="fcol" style="left:820px"><h4>Stay Tuned With Us</h4><p>Receive latest offers and news</p><div class="sub"><span>Enter Your Email</span><i></i></div></div>
</footer>
<footer class="bottom">
  <span class="copy">© COPYRIGHT 2018 VINDABORGPRENT. ALL RIGHTS RESERVED.</span>
  <div class="social"><i></i><i></i><i></i><i></i></div>
</footer>

</body>
</html>
```